Fotograf sucht Gutschein-Design
Schnell, unkomplizierte Abwicklung und ich habe ein wunderschönes Design erhalten.
Zielgruppe
Bin Fotograf spezialisiert auf Pärchen und Hochzeitsfotos
Aufgabenstellung
Möchte einen neuen Gutschein für meine Zwecke haben. Sollte zu meinem fotografischen Stil passen, hell/ freundlich/ Retro? Vintage? Kann auch gerne 'Verzierung' mit Blümchen/ Zweige enthalten wenns passt. am besten ein wenig auf meiner Homepage orientieren >>> www.tobiasrandecker.com - Auch meine Logo/ Firmendaten sollten wo passend platziert sein. Mein Logo/ und Fotos füge ich bei und können wie es gut passt verwendet werden. Das auf dem Einzelbild bin ich, falls es wo passt wäre es toll. Schriftmäßig sollte es natürlich irgendwie das Wort Gutschein enthalten. Dann noch 'von' und 'für' und ein Feld wo ich händisch die Gutscheinnummer eintragen kann. Das Format/ Form überlasse ich auch ganz euch aber werde voraussichtlich bei karteneck bestellen. (Falls es um das finden des passenden Formats/ Form geht). Bei Fragen könnt ihr euch gerne jederzeit melden.

```html
<!DOCTYPE html>
<html lang="de">
<head>
<meta charset="utf-8">
<title>Gutschein – Tobias Randecker Fotografie</title>
<link href="https://fonts.googleapis.com/css2?family=Antonio:wght@400;500&family=Montserrat:wght@500&display=swap" rel="stylesheet">
<style>
  :root {
    --page: #ffffff;
    --card-white: #ffffff;
    --card-sand: #d8c6ab;
    --gold: #b8a27f;
    --ink: #4a4a4a;
    --ink-dark: #2b2b2b;
  }
  * { box-sizing: border-box; margin: 0; padding: 0; }
  html, body {
    width: 1200px; height: 1153px; overflow: hidden;
    background: var(--page);
  }
  .canvas { position: relative; width: 1200px; height: 1153px; }

  .card {
    position: absolute; top: 272px; width: 497px; height: 700px;
    box-shadow: 0 8px 22px rgba(0,0,0,0.16);
    overflow: hidden;
  }
  .card--front { left: 76px; background: var(--card-white); }
  .card--back  { left: 624px; background: var(--card-sand); }

  .branch {
    position: absolute; border-radius: 40px;
  }
  .card--front .branch {
    left: 54px; top: 78px; width: 443px; height: 128px;
    background: linear-gradient(90deg, rgba(184,162,127,0.12), rgba(184,162,127,0.32));
  }
  .card--back .branch {
    left: 56px; top: 481px; width: 441px; height: 128px;
    background: linear-gradient(90deg, rgba(43,43,43,0.08), rgba(43,43,43,0.2));
  }

  .voucher-title {
    position: absolute; left: 0; top: 254px; width: 100%;
    text-align: center; white-space: nowrap;
    font-family: "Antonio", sans-serif; font-weight: 500;
    font-size: 62px; line-height: 1; letter-spacing: 17px;
    padding-left: 17px;
    color: var(--ink);
  }

  .field {
    position: absolute; left: 64px; width: 369px; height: 42px;
    border: 1.5px solid var(--gold);
  }
  .field--from { top: 421px; }
  .field--to { top: 506px; }
  .field--number { top: 597px; left: 63px; width: 372px; }

  .field__label {
    position: absolute; top: -12px; left: 50%; transform: translateX(-50%);
    background: var(--card-white);
    padding: 0 6px 0 14px;
    font-family: "Antonio", sans-serif; font-weight: 500;
    font-size: 20px; line-height: 22px; letter-spacing: 10px;
    color: var(--ink); white-space: nowrap;
  }
  .field--number .field__label { letter-spacing: 7px; padding: 0 5px 0 12px; }

  .field__heart {
    position: absolute; width: 26px; height: 22px; top: -12px;
    background: var(--card-white); padding: 0 3px;
  }
  .field--from .field__heart { left: 329px; }
  .field--to .field__heart { left: 15px; }

  .frame {
    position: absolute; left: 16px; top: 16px; width: 467px; height: 671px;
    border: 2px solid var(--ink-dark);
  }

  .logo-mark {
    position: absolute; left: 140px; top: 107px; width: 223px; height: 205px;
    border-radius: 18px;
    background: linear-gradient(180deg, rgba(74,74,74,0.10), rgba(74,74,74,0.18));
  }

  .brand {
    position: absolute; left: 0; width: 100%; text-align: center;
    white-space: nowrap; color: var(--ink); line-height: 1;
  }
  .brand__name {
    top: 350px;
    font-family: "Antonio", sans-serif; font-weight: 400;
    font-size: 38px; letter-spacing: 5px; padding-left: 5px;
  }
  .brand__tag {
    top: 401px;
    font-family: "Montserrat", sans-serif; font-weight: 500;
    font-size: 13px; letter-spacing: 7px; padding-left: 7px;
    color: var(--ink-dark);
  }
</style>
</head>
<body>
<main class="canvas">

  <section class="card card--front" aria-label="Gutschein Vorderseite">
    <div class="branch" role="img" aria-label="Zierzweig mit Blättern in Gold"></div>
    <h1 class="voucher-title">GUTSCHEIN</h1>

    <div class="field field--from">
      <span class="field__label">VON</span>
      <svg class="field__heart" viewBox="0 0 24 20" aria-hidden="true">
        <path d="M12 19 C4 13 1 10 1 6 C1 3 3 1 6 1 C9 1 11 3 12 5 C13 3 15 1 18 1 C21 1 23 3 23 6 C23 10 20 13 12 19Z" fill="var(--gold)"/>
      </svg>
    </div>

    <div class="field field--to">
      <svg class="field__heart" viewBox="0 0 24 20" aria-hidden="true">
        <path d="M12 19 C4 13 1 10 1 6 C1 3 3 1 6 1 C9 1 11 3 12 5 C13 3 15 1 18 1 C21 1 23 3 23 6 C23 10 20 13 12 19Z" fill="var(--gold)"/>
      </svg>
      <span class="field__label">FÜR</span>
    </div>

    <div class="field field--number">
      <span class="field__label">GUTSCHEINNUMMER</span>
    </div>
  </section>

  <section class="card card--back" aria-label="Gutschein Rückseite">
    <div class="frame"></div>
    <div class="logo-mark" role="img" aria-label="Platz für das Logo-Signet des Fotografen"></div>
    <p class="brand brand__name">TOBIAS RANDECKER</p>
    <p class="brand brand__tag">FOTOGRAFIE</p>
    <div class="branch" role="img" aria-label="Zierzweig mit Blättern in Dunkelgrau"></div>
  </section>

</main>
</body>
</html>
```